依頼詳細
健康食品のノニジュースのLPの制作をお願いします。
これまでのターゲット顧客層は50〜60代後半でしたが、インターネットでの拡販/新規顧客獲得の狙いなので30〜40代後半をイメージしたLPをお願いします。

【ノニジュース】
特徴としては醗酵させたノニジュースには豊富なアミノ酸や140種類を超える栄養素を含んでいます。
特徴
①ノニ販売15年以上の国内古参企業で累計50万本以上販売

②100%にこだわり、余計な添加物は一切無し。

③原料にもこだわり、無農薬、世界最高基準の厳しいオーガニックKRT認定を受けたもののみを使用。

④通常3ヶ月熟成させたものを絞っておりますが、弊社商品サラくる醗酵原液STARは倍の期間の6ヶ月熟成させたものを絞っております。栄養価も高くノニフリークのお客様も数多くの方がご愛飲頂いています。

⑤弊社では現地農場と直接契約しいるので余計な中間業者が存在せず、その分コストを抑えることで、続けやすいお値段でご提供させていただいております。

⑥原産地のニウエ島では島にあるもののみでノニの栽培を行っており、栄養価は他産地のノニに比べ非常にミネラルが豊富で、糖度も6.9~8.0と高い数値を出しております。
サイトURL
http://sarakuru-home.jp/ic/star
ページ数
4ページ
希望イメージ
シンプル 複雑
単色 カラフル
暗い 明るい
日常 高級
遊び心 厳粛
未来的 伝統的
女性的 男性的
希望する色
茶系、緑系、黄・オレンジ系
納品ファイル
• イラストレーター形式 (.ai)
• フォトショップ形式 (.psd)
補足説明
お客様の声は当方で保有しておりますので、5名分程入力する箇所を作成してください。
■ 選んだ理由

トータルデザインが当方の希望と合致いたしました。
詳細の変更デザイン追加などにも柔軟にご対応いただきました。

■ 提案者全員のお礼・コメント

この度は当案件にご協力いただきありがとうございました。
今回の案件が私ども初めての仕事依頼でしたので、ご提案いただきました
すべてのタスクネスターの方々のクオリティの高さに驚きました。
今後もTasknestで仕事を積極的に依頼していく予定でございますので
また機会がございましたらぜひご提案の程お待ちしております。
有難うございました。

```html
<!DOCTYPE html>
<html lang="ja">
<head>
<meta charset="utf-8">
<title>サラくる醗酵原液STAR</title>
<link rel="stylesheet" href="https://fonts.googleapis.com/css2?family=Noto+Sans+JP:wght@400;700;900&display=swap">
<style>
  :root {
    --green-dark: #1f9a2a;
    --green-light: #7ad84a;
    --red: #e0141c;
    --band: #b5434c;
    --yellow: #fff200;
    --pink-bg: #f6d6d6;
    --pink-box: #f3aaa8;
    --pink-line: #d98686;
    --ink: #111;
    --white: #fff;
    --bottle-dark: #2a0f14;
    --bottle-mid: #6a1c26;
  }
  * { box-sizing: border-box; margin: 0; padding: 0; }
  html, body { width: 1200px; height: 3984px; overflow: hidden; }
  body {
    position: relative;
    font-family: "Noto Sans JP", sans-serif;
    color: var(--ink);
    background: var(--white);
  }
  .abs { position: absolute; white-space: nowrap; }

  .hero { left: 0; top: 0; width: 1200px; height: 700px;
    background: linear-gradient(#fff 0%, #f1f1f1 60%, #e4e4e4 100%); }
  .brand-bar { left: 0; top: 0; width: 860px; height: 112px;
    background: linear-gradient(90deg, var(--green-dark), var(--green-light));
    color: var(--white); font-size: 44px; font-weight: 700; font-style: italic;
    line-height: 112px; padding-left: 22px; }
  .sales-box { left: 60px; top: 140px; width: 580px; height: 230px;
    background: var(--yellow); transform: rotate(-3deg);
    box-shadow: 10px 10px 0 #9a9a9a;
    color: var(--red); font-size: 130px; font-weight: 900;
    text-align: center; line-height: 230px; letter-spacing: 4px; }
  .sales-sub { left: 120px; top: 395px; font-size: 40px; font-weight: 700; }
  .hero-title { left: 120px; top: 470px; font-size: 60px; font-weight: 900; line-height: 1.3; }

  .order-btn { background: linear-gradient(#ff3b3b, var(--red) 55%, #b50008);
    color: var(--white); font-weight: 700; text-align: center;
    border-radius: 10px; box-shadow: 0 6px 0 #7d0005; }
  .order-btn.small { left: 730px; top: 604px; width: 330px; height: 82px;
    font-size: 38px; line-height: 82px; }
  .order-btn.large { left: 300px; top: 3800px; width: 600px; height: 160px;
    font-size: 60px; line-height: 160px; }

  .bottle { border-radius: 40px 40px 24px 24px;
    background: linear-gradient(90deg, var(--bottle-dark), var(--bottle-mid) 45%, var(--bottle-dark)); }
  .bottle.top { left: 870px; top: 24px; width: 200px; height: 570px; }
  .bottle.bottom { left: 920px; top: 3390px; width: 200px; height: 400px; }

  .band { left: 0; width: 1200px; height: 50px; background: var(--band);
    color: var(--white); font-size: 34px; font-weight: 700;
    line-height: 50px; padding-left: 14px; }

  .point { top: 780px; width: 360px; height: 360px; border: 2px solid #9bcf7a;
    background: linear-gradient(160deg, #c9f59c, #5fc92b 55%, #2f9a1a); }
  .point-head { height: 64px; background: var(--white);
    display: flex; align-items: center; gap: 12px; padding-left: 10px;
    font-size: 26px; font-weight: 700; }
  .point-num { width: 44px; height: 44px; border-radius: 50%;
    background: var(--red); color: var(--white); text-align: center;
    line-height: 44px; font-size: 26px; flex: none; }

  .voices { left: 0; top: 1216px; width: 1200px; height: 780px; background: var(--pink-bg); }
  .voice { left: 30px; width: 1140px; font-size: 33px; line-height: 1.5;
    padding: 14px 22px; border: 2px solid var(--pink-line); white-space: normal; }
  .voice.featured { top: 1232px; height: 150px; background: var(--white); }
  .voice.placeholder { height: 124px; background: var(--pink-box); word-break: break-all; }
  .voice-age { position: absolute; right: 22px; bottom: 6px; font-size: 22px; }

  .photo { left: 80px; width: 1040px; }
  .photo.tree { top: 2068px; height: 692px;
    background: linear-gradient(#cfe3f2 0%, #9fc4a2 40%, #4f8a3a 70%, #b8a98c 100%); }
  .photo.barrels { top: 2760px; height: 640px;
    background: linear-gradient(#7b3a3a, #a56b6b 45%, #d8d2cc 100%); }

  .closing-line { left: 80px; top: 3480px; font-size: 66px; font-weight: 900; }
  .closing-main { left: 80px; top: 3590px; font-size: 66px; font-weight: 900; line-height: 1.3; }
  .closing-main em { font-style: normal; color: var(--green-dark); font-size: 100px; }
</style>
</head>
<body>
  <div class="abs hero"></div>
  <div class="abs brand-bar">サラくる醗酵原液STAR</div>
  <div class="abs bottle top" role="img" aria-label="商品ボトルの写真"></div>
  <div class="abs sales-box">５０万本</div>
  <div class="abs sales-sub">以上売れています！</div>
  <h1 class="abs hero-title">世界が認めたノニジュース</h1>
  <div class="abs order-btn small">ご注文はこちら</div>

  <div class="abs band" style="top:712px">働き盛りのアナタにおすすめ！元気が出る3つのポイント</div>
  <div class="abs point" style="left:30px"><div class="point-head"><span class="point-num">1</span>140種類以上のアミノ酸</div></div>
  <div class="abs point" style="left:420px"><div class="point-head"><span class="point-num">2</span>100%天然ジュース</div></div>
  <div class="abs point" style="left:810px"><div class="point-head"><span class="point-num">3</span>長期熟成だから</div></div>

  <div class="abs band" style="top:1168px">お客様からの喜びの声をお届けします！（利用者の感想です）</div>
  <div class="abs voices"></div>
  <div class="abs voice featured">つらかった早起きが、全然苦になくなりました。ノニジュースを毎日飲んでいるおかげだと思います。<span class="voice-age">30代女性</span></div>
  <div class="abs voice placeholder" style="top:1400px">○○○○○○○○○○○○○○○○○○○○○○○○○○○○○○○○○○○○○○○○○○○○○。</div>
  <div class="abs voice placeholder" style="top:1550px">○○○○○○○○○○○○○○○○○○○○○○○○○○○○○○○○○○○○○○○○○○○○○。</div>
  <div class="abs voice placeholder" style="top:1700px">○○○○○○○○○○○○○○○○○○○○○○○○○○○○○○○○○○○○○○○○○○○○○。</div>
  <div class="abs voice placeholder" style="top:1850px">○○○○○○○○○○○○○○○○○○○○○○○○○○○○○○○○○○○○○○○○○○○○○。</div>

  <div class="abs band" style="top:1996px">140種類のアミノ酸が健康の源！長期熟成で作られる味わい</div>
  <div class="abs photo tree" role="img" aria-label="農園に立つノニの木の写真"></div>
  <div class="abs photo barrels" role="img" aria-label="熟成中のノニを収めた樽が並ぶ写真"></div>

  <div class="abs closing-line">ノニジュースで</div>
  <div class="abs closing-main"><em>健康的</em>な毎日を！</div>
  <div class="abs bottle bottom" role="img" aria-label="商品ボトルの写真"></div>
  <div class="abs order-btn large">ご注文はこちら</div>
</body>
</html>
```